Asia based real estate financing firm needs and AWESOME design for a biz card -Harbor Lending Circle

Looking for a stylish, & corporate-looking business card for a real estate financing brokerage firm in Asia, offering global mortgage loans. I uploaded our current logos. We would like to add a splash of color (perhaps the house icon) or any other suggestions are open. For the winning designer, we have a lot of work! Thanks and best of luck!

Target Market(s)

Real estate investors globally. We want to look more like a BANK and NOT a real estate company. Please don't play up on a "house" design.

Industry/Entity Type

Banking

Contact Information for Business Card

Harbor Lending Circle
Peter Wilks
Co-Founder | Partner

14 Cassia Lane, Suite 310
Singapore 047219
www.hlc-example.asia
peterwilks@hlc-example.asia
+65 555-0142
WeChat: peterwilks

Colors

Designer to choose colors to be used in the design.

Requirements
Must have
• Must have the standard business requirements for a card; name, address, email, etc
• Can be horizontal or vertical.
Nice to have
• It would be great to see some sort of variation to the logo with a pop of color. Red is good as we're in Asia, however, other options work as well.
• Our tag line is - Borderless mortgages. It doesn't have to be on the card but might be nice.
• I'd like to start seeing our tagline within the cards as well. - Borderless mortgages.
• Also, please add our location. The location for this card is Singapore so perhaps it can be highlighted or emphasised in some way.
• Singapore | Hong Kong | Shanghai | Manila
• As we will soon open an office in Shanghai, having an option for both languages would be great.
Should not have
• I'm exceited and open to your creativity ... knock it out of the park!

```html
<!DOCTYPE html>
<html lang="en">
<head>
<meta charset="utf-8">
<title>Harbor Lending Circle – Business Card</title>
<link rel="stylesheet" href="https://fonts.googleapis.com/css2?family=Open+Sans:wght@400;600;700&display=swap">
<style>
  :root {
    --page-bg: #e8eef6;
    --card-white: #ffffff;
    --brand-blue: #1f6fc4;
    --brand-blue-deep: #0f57a8;
    --brand-blue-light: #3f8fe0;
    --ink-grey: #5a6470;
    --icon-blue: #2a78c8;
    --on-blue: #ffffff;
  }
  * { box-sizing: border-box; margin: 0; padding: 0; }
  html, body {
    width: 1200px; height: 914px; overflow: hidden;
    background: var(--page-bg);
    font-family: "Open Sans", Arial, sans-serif;
  }
  .card-pair {
    position: absolute; top: 167px; left: 230px;
    display: flex; gap: 80px;
  }
  .card {
    width: 330px; height: 580px; position: relative;
    box-shadow: 0 10px 30px rgba(20, 50, 90, 0.18);
  }
  .card--front { background: var(--card-white); }
  .card--back {
    background: linear-gradient(150deg, var(--brand-blue-light) 0%, var(--brand-blue) 45%, var(--brand-blue-deep) 100%);
    color: var(--on-blue);
  }
  .wordmark {
    position: absolute; left: 0; right: 0; top: 110px;
    display: flex; flex-direction: column; align-items: center; gap: 14px;
    font-weight: 700; font-size: 25px; line-height: 1.2; text-align: center;
  }
  .wordmark__square { width: 26px; height: 26px; }
  .card--front .wordmark { color: var(--brand-blue); }
  .card--front .wordmark__square { background: var(--brand-blue); }
  .card--back .wordmark { color: var(--on-blue); }
  .card--back .wordmark__square { background: var(--on-blue); }

  .contact-list {
    position: absolute; left: 38px; top: 300px;
    list-style: none; font-size: 13px; color: var(--ink-grey);
  }
  .contact-list li { display: flex; align-items: center; gap: 10px; margin-bottom: 12px; }
  .contact-list .icon { width: 14px; height: 14px; flex: none; }
  .contact-list .address { color: var(--brand-blue); font-weight: 700; }
  .contact-list .address-line { margin-left: 24px; margin-top: -8px; }

  .holder {
    position: absolute; left: 0; right: 0; bottom: 80px; text-align: center;
  }
  .holder__name { font-size: 21px; font-weight: 700; }
  .holder__title { font-size: 15px; font-weight: 400; margin-top: 4px; }
</style>
</head>
<body>
<main class="card-pair">
  <section class="card card--front" aria-label="Card front with contact details">
    <div class="wordmark"><span class="wordmark__square"></span><span>Harbor Lending<br>Circle</span></div>
    <ul class="contact-list">
      <li class="address">
        <svg class="icon" viewBox="0 0 14 14"><circle cx="7" cy="7" r="7" fill="var(--icon-blue)"/><path d="M7 3a2.4 2.4 0 0 0-2.4 2.4C4.6 7.2 7 10.5 7 10.5s2.4-3.3 2.4-5.1A2.4 2.4 0 0 0 7 3z" fill="#fff"/></svg>
        <span>14 Cassia Lane, Suite 310</span>
      </li>
      <li class="address address-line"><span>Singapore 047219</span></li>
      <li>
        <svg class="icon" viewBox="0 0 14 14"><circle cx="7" cy="7" r="7" fill="var(--icon-blue)"/><path d="M4.5 3.5h1.6l.7 1.8-.9.7a5 5 0 0 0 2.1 2.1l.7-.9 1.8.7v1.6c0 .4-.4.7-.8.7A6 6 0 0 1 3.8 4.3c0-.4.3-.8.7-.8z" fill="#fff"/></svg>
        <span>+65 555-0142</span>
      </li>
      <li>
        <svg class="icon" viewBox="0 0 14 14"><circle cx="7" cy="7" r="7" fill="var(--icon-blue)"/><rect x="3.5" y="4.5" width="7" height="5" fill="#fff"/><path d="M3.5 4.5 7 7.3l3.5-2.8" fill="none" stroke="var(--icon-blue)" stroke-width="0.8"/></svg>
        <span>peterwilks@hlc-example.asia</span>
      </li>
      <li>
        <svg class="icon" viewBox="0 0 14 14"><circle cx="7" cy="7" r="7" fill="var(--icon-blue)"/><circle cx="7" cy="7" r="3.5" fill="none" stroke="#fff" stroke-width="0.9"/><path d="M3.5 7h7M7 3.5c-1.5 2-1.5 5 0 7M7 3.5c1.5 2 1.5 5 0 7" fill="none" stroke="#fff" stroke-width="0.8"/></svg>
        <span>www.hlc-example.asia</span>
      </li>
      <li>
        <svg class="icon" viewBox="0 0 14 14"><circle cx="7" cy="7" r="7" fill="var(--icon-blue)"/><path d="M3.5 6.3c0-1.5 1.6-2.6 3.5-2.6s3.5 1.1 3.5 2.6S8.9 8.9 7 8.9c-.4 0-.8 0-1.1-.1L4.3 10l.4-1.5c-.8-.5-1.2-1.3-1.2-2.2z" fill="#fff"/></svg>
        <span>WeChat: peterwilks</span>
      </li>
    </ul>
  </section>

  <section class="card card--back" aria-label="Card back with name and title">
    <div class="wordmark"><span class="wordmark__square"></span><span>Harbor Lending<br>Circle</span></div>
    <div class="holder">
      <p class="holder__name">Peter Wilks</p>
      <p class="holder__title">Co-Founder | Partner</p>
    </div>
  </section>
</main>
</body>
</html>
```